Cruise Booking Website

Cruise search and booking website

This project is a redesign of a cruise booking website we did a few years ago.

The current website is located here: http://voyage.pixelmarsh.com/en/

It's not fully functional but gives you ad idea how miserable the old design was.

All the information about cruises, cruise lines, destinations, ports and shore excursions will be similar to http://www.sailorbay.com/
Actual search pages (form, results, single result, sailing and cabin selection, ship info, booking) will have EXACTLY the same info as sailorbay.com

We like the style of http://harborvoyagehub.com, it's quite modern, good spacing, not overloaded with information. So you can use it as an example of what we like, not what we want as a final result for us. Please, don't copy it. The result should not be possible to resemble the harborvoyagehub.com, because our site has to be unique. This is important!
If you submit a design that clearly reminds another cruise site it will be rejected!

Also the mockup provided is just to give you the basic structure and show what information has to be present on the page. It doesn't mean the layout has to be the same as a mockup. The layout is up to the designer.

I've updated the mockup to be more generic so it doesn't confuse you:
https://www.filecrate.net/s/k7q2mz9pw4tnb3x/Home%20page.png

When you're adding social sharing icons like chatterbox/peeplet you have to use chinese ones instead:
https://www.filecrate.net/s/h3rt8wyd6jcl0fe/chinese-social-icons.png
Originals: http://shrtlk.example/qRmT

We'll start with home page first and after it's approved inner pages can be designed.

I know the cost of the project doesn't look high, but the task is straight forward and doesn't require to be very original, it's better to follow existing design and layout patterns that proved to work well.
That's why I encourage you to choose a template to build the design on top of one of https://themequarry.net/ themes if it will save the design work, will be easier and faster for you. So it will be more like a customization than a new design from scratch.

Mockups, site map and logo files:
- https://www.filecrate.net/sh/50xb7vq1ndtpkez/RmwuHp8Zq3

Website tree:
- https://papers.quillnet.example/document/d/8vTrXk2MqLpZ4wNsB7yHcE1oUjFgD9aR_QbVtnWm/edit?usp=sharing
Updates

So far a lot of designs are just copying http://www.harborvoyagehub.com/ - we don't like it!

We like the style of harborvoyagehub.com, it's quite modern, good spacing, not overloaded with information. So you can use it as an example of what we like, not what we want as a final result for us. Please, don't copy it. The result should not be possible to resemble the harborvoyagehub.com, because our site has to be unique. This is important!

Target Market(s)

Chinese travellers

Industry/Entity Type

Build

Requirements
Must have
• * White, blue and red
* Large spacing, not too much information cramped into a small space like sailorbay.com or the current website
* More "hidden" info in popups, tabs and so on, so not to many things are visible at the same time
* Compatible with lumen framekit styling (for easier coding):
- http://lumenkit.example.io/framework/index.html
- http://skinvault.net/
* Feel free to propose to build the design on top of one of https://themequarry.net/ themes if it will save the design work, will be easier and faster for you

```html
<!DOCTYPE html>
<html lang="en">
<head>
<meta charset="utf-8">
<title>BlueWake – Cruise Booking</title>
<link href="https://fonts.googleapis.com/css2?family=Open+Sans:ital,wdth,wght@0,75..100,300..800;1,75..100,300..800&display=swap" rel="stylesheet">
<style>
:root{
  --sky-top:#2f6fc0;
  --sky-mid:#7fa9dc;
  --brand-blue:#1f6aa6;
  --nav-blue:#2b679f;
  --nav-active:#4aa6c8;
  --link-blue:#2a8ec0;
  --accent-red:#d9213f;
  --dark-panel:#3b3c3e;
  --tab-grey:#cbdae6;
  --content-bg:#f5f5f5;
  --news-bg:#dde7ef;
  --footer-blue:#2d6aa0;
  --footer-dark:#275d8e;
  --text:#222;
  --white:#fff;
}
*{box-sizing:border-box;margin:0;padding:0}
html,body{width:1114px;height:1200px;overflow:hidden}
body{font-family:"Open Sans",sans-serif;color:var(--text);
  background:linear-gradient(180deg,var(--sky-top) 0%,var(--sky-mid) 45%,#e6eef8 70%,#2f63a8 100%);position:relative}
.page{position:absolute;left:159px;top:0;width:796px;height:1200px;background:var(--white)}
.abs{position:absolute;white-space:nowrap}

.topbar{left:0;top:11px;width:796px;height:24px;background:#d8e2ea;font-size:11px;color:var(--link-blue);text-align:right;padding:4px 24px 0 0}
.topbar span{margin-left:10px}
.topbar .sep{color:#8aa}

.brand{left:19px;top:52px;display:flex;align-items:center;gap:8px}
.brand-dot{width:58px;height:58px;border-radius:50%;background:var(--brand-blue)}
.brand-name{font-size:40px;font-weight:700;color:var(--brand-blue);line-height:1}
.brand-url{left:88px;top:98px;font-size:10px;font-weight:700;color:var(--brand-blue)}

.phone{left:550px;top:60px;display:flex;align-items:center;gap:10px;color:var(--accent-red);font-size:31px;font-weight:700}
.socials{display:flex;gap:4px}
.socials i{display:block;width:19px;height:19px;border-radius:3px}
.s1{background:#3b82d6}.s2{background:#e0542e}.s3{background:#4aa0d8}.s4{background:#5aa83a}.s5{background:#2f6ec4}.s6{background:#5cb82f}

.nav{left:0;top:135px;width:732px;height:28px;background:var(--nav-blue);display:flex}
.nav a{color:var(--white);font-size:13px;text-decoration:none;padding:0 15px;line-height:28px;border-right:1px solid #255c8f}
.nav a.active{background:var(--nav-active)}
.search{left:668px;top:135px;width:98px;height:28px;background:var(--white);font-size:11px;font-style:italic;color:#888;padding:7px 0 0 14px}
.search-btn{left:766px;top:135px;width:30px;height:28px;background:var(--accent-red)}

.hero{left:0;top:163px;width:558px;height:303px;background:linear-gradient(180deg,#233654 0%,#4a4a55 40%,#c9864a 62%,#2b2a30 100%)}
.hero-caption{left:0;top:394px;width:455px;height:61px;background:rgba(20,20,20,.75);color:var(--white);font-size:29px;font-weight:700;font-stretch:82%;letter-spacing:-.6px;line-height:61px;padding:0 0 0 24px;overflow:hidden}

.finder{left:558px;top:163px;width:238px;height:303px;background:var(--dark-panel)}
.finder h3{position:absolute;left:17px;top:28px;font-size:16px;font-weight:400;color:#eee}
.finder .rule{position:absolute;left:17px;top:54px;width:204px;height:1px;background:#555}
.select{position:absolute;left:17px;width:203px;height:27px;background:#f2f5f8;font-size:11px;color:var(--brand-blue);padding:6px 0 0 8px}
.select::after{content:"";position:absolute;right:0;top:0;width:28px;height:27px;border-left:1px solid #ccc}
.adv-link{left:572px;top:400px;font-size:10.5px;color:#ddd;text-decoration:underline}
.search-cruises{left:658px;top:393px;width:121px;height:32px;background:var(--accent-red);color:var(--white);font-size:12px;padding:8px 0 0 10px}
.search-cruises svg{position:absolute;right:0;top:0;border-left:1px solid #b51a33}

.tabs{left:0;top:466px;width:558px;height:46px;display:flex}
.tabs div{font-size:12px;display:flex;align-items:center;justify-content:center;background:var(--tab-grey);border-left:1px solid #fff}
.tabs .on{background:var(--content-bg);border:0}

.content{left:0;top:512px;width:558px;height:283px;background:var(--content-bg)}
.photo{left:27px;top:564px;width:286px;height:184px;background:linear-gradient(180deg,#6fa6cf 0%,#cfe0ea 45%,#c9a47a 60%,#d9c3a1 100%);border:4px solid #e6e6e6}
.book-title{left:323px;top:560px;font-size:26px;color:var(--link-blue)}
.book-text{left:326px;top:602px;width:220px;font-size:11px;line-height:16px;white-space:normal}
.perks{left:326px;top:652px;list-style:none;font-size:12px;color:var(--link-blue)}
.perks li{height:24px;display:flex;align-items:center;gap:8px}
.perks li::before{content:"+";display:inline-flex;width:12px;height:12px;border:1.5px solid var(--accent-red);border-radius:50%;color:var(--accent-red);font-size:10px;line-height:9px;justify-content:center}

.newsletter{left:558px;top:466px;width:238px;height:329px;background:var(--news-bg)}
.nl-title{left:585px;top:488px;font-size:17px;color:var(--link-blue)}
.nl-photo{left:584px;top:522px;width:189px;height:92px;background:linear-gradient(180deg,#4f7fb8 0%,#c9d8e8 55%,#23508a 100%)}
.nl-text{left:586px;top:625px;width:180px;font-size:12px;line-height:16px;white-space:normal}
.field{background:var(--white);border:1px solid #d8dde2;font-size:12px;font-style:italic;color:#666;padding:7px 0 0 10px}
.subscribe{left:586px;top:743px;width:189px;height:29px;background:var(--accent-red);color:var(--white);font-size:15px;text-align:center;line-height:29px}

.partners{left:0;top:795px;width:796px;height:77px;background:#ececec}
.partners-label{left:0;top:795px;width:112px;height:77px;background:var(--white);padding:10px 0 0 14px;color:#555;line-height:1}
.partners-label small{font-size:14px;display:block}
.partners-label b{font-size:20px;font-weight:400}
.arrow{top:842px;width:24px;height:23px;background:#bbb;color:#fff;font-size:14px;text-align:center;line-height:22px}
.badge{top:810px;width:109px;height:44px;background:var(--white);border:2px solid #ddd}

.footer-brand{left:0;top:872px;width:796px;height:90px;background:var(--footer-blue)}
.fb-dot{left:31px;top:889px;width:55px;height:55px;border-radius:50%;background:#eaf3fa}
.fb-name{left:107px;top:897px;font-size:32px;font-weight:700;color:var(--white)}
.fb-tag{left:295px;top:906px;font-size:17px;color:var(--white)}
.footer{left:0;top:962px;width:796px;height:200px;background:repeating-linear-gradient(45deg,#2d6aa0 0 2px,#3070a6 2px 4px)}
.footer-head{left:0;top:965px;width:796px;height:30px;background:var(--footer-dark)}
.fcol{top:972px;color:var(--white);font-size:11px}
.fcol h4{font-size:14px;font-weight:600;margin-bottom:16px}
.fcol li{list-style:none;height:19px;padding-left:3px}
.contact li{height:19.5px;display:flex;align-items:center;gap:6px}
.ffield{position:absolute;left:593px;width:188px;background:#245a8c;font-size:10px;font-style:italic;color:#a9c3dc;padding:6px 0 0 9px}
.send{left:717px;top:1130px;width:64px;height:22px;background:#4a93c6;color:var(--white);font-size:12px;text-align:center;line-height:22px}
.copyright{left:0;top:1162px;width:796px;height:38px;background:#2a6398;color:var(--white);font-size:9px;text-align:center;line-height:30px}
</style>
</head>
<body>
<div class="page">
  <div class="abs topbar"><span>&#10162; Sign in</span><span class="sep">|</span><span>sign up</span></div>

  <div class="abs brand"><div class="brand-dot"></div><div class="brand-name">BlueWake</div></div>
  <div class="abs brand-url">www.bluewakecruise.com</div>

  <div class="abs phone">
    <svg width="27" height="27" viewBox="0 0 27 27"><rect width="27" height="27" rx="5" fill="#d9213f"/><path d="M8 6c1 0 2 3 2 4s-2 1-1 3 3 4 4 4 2-2 3-1 3 2 3 3-2 3-4 2-6-4-8-7-1-8 1-8z" fill="#fff"/></svg>
    4008 215 390
  </div>
  <div class="abs socials" style="left:646px;top:98px"><i class="s1"></i><i class="s2"></i><i class="s3"></i><i class="s4"></i><i class="s5"></i><i class="s6"></i></div>

  <nav class="abs nav">
    <a class="active">Home</a><a>Lines</a><a>Shores</a><a>Destinations</a><a>FAQ</a><a>News</a><a>Promotions</a><a>Booking</a><a style="border:0">Blog</a>
  </nav>
  <div class="abs search">Search...</div>
  <div class="abs search-btn"><svg width="30" height="28"><circle cx="16" cy="12" r="6" fill="none" stroke="#fff" stroke-width="2"/><line x1="12" y1="16" x2="8" y2="21" stroke="#fff" stroke-width="2"/></svg></div>

  <div class="abs hero" role="img" aria-label="Illuminated cruise yacht moored in a harbour at dusk"></div>
  <div class="abs hero-caption">All Inclusive Vacation Packages</div>

  <div class="abs finder">
    <h3>Find Your Cruise</h3>
    <svg style="position:absolute;left:212px;top:32px" width="15" height="15"><circle cx="7.5" cy="7.5" r="6.5" fill="none" stroke="#ddd"/><path d="M7.5 4v7M4.5 8l3 3 3-3" stroke="#ddd" fill="none"/></svg>
    <div class="rule"></div>
    <div class="select" style="top:68px">Popular Destinations</div>
    <div class="select" style="top:105px">Any Length</div>
    <div class="select" style="top:142px">Any Length</div>
    <div class="select" style="top:179px">Any Cruise Line</div>
  </div>
  <div class="abs adv-link">Advanced Search</div>
  <div class="abs search-cruises">Search Cruises<svg width="28" height="32"><circle cx="15" cy="14" r="5" fill="none" stroke="#fff" stroke-width="1.8"/><line x1="11.5" y1="17.5" x2="8" y2="21" stroke="#fff" stroke-width="1.8"/></svg></div>

  <div class="abs tabs">
    <div class="on" style="width:105px">Book with us</div>
    <div style="width:96px">Deals</div>
    <div style="width:98px">Pakages</div>
    <div style="width:98px">News</div>
    <div style="width:161px">First Time Cruiser?</div>
  </div>
  <div class="abs content"></div>
  <div class="abs photo" role="img" aria-label="Couple sitting on a sandy beach by the sea"></div>
  <div class="abs book-title">Book with us</div>
  <p class="abs book-text">We are the most advanced cruise booking provider in China</p>
  <ul class="abs perks">
    <li>Great prices</li><li>Fast booking processing</li><li>20 cruise lines</li><li>Destinations around the world</li>
  </ul>

  <div class="abs newsletter"></div>
  <div class="abs nl-title">Cruise Deals Newsletter</div>
  <div class="abs nl-photo" role="img" aria-label="Large cruise ship at sea"></div>
  <p class="abs nl-text">Subscribe an recive the beals cruise deals now!</p>
  <div class="abs field" style="left:586px;top:666px;width:189px;height:29px">Name</div>
  <div class="abs field" style="left:586px;top:704px;width:189px;height:29px">Email</div>
  <div class="abs subscribe">Subscribe</div>

  <div class="abs partners"></div>
  <div class="abs partners-label"><small>Our Reliable</small><b>Partners</b></div>
  <div class="abs arrow" style="left:45px">&#8249;</div>
  <div class="abs arrow" style="left:70px;background:#999">&#8250;</div>
  <div class="abs badge" style="left:123px"></div>
  <div class="abs badge" style="left:248px"></div>
  <div class="abs badge" style="left:373px"></div>
  <div class="abs badge" style="left:498px"></div>
  <div class="abs badge" style="left:623px"></div>
  <div class="abs badge" style="left:748px;width:48px;border-right:0"></div>

  <div class="abs footer-brand"></div>
  <div class="abs fb-dot"></div>
  <div class="abs fb-name">BlueWake</div>
  <div class="abs fb-tag">We are the most advanced cruise booking provider in China</div>
  <div class="abs footer"></div>
  <div class="abs footer-head"></div>

  <div class="abs fcol" style="left:16px"><h4>Useful pages</h4><ul><li>About us</li><li>Contact us</li><li>Blog</li><li>FAQ</li><li>Terms of Service</li><li>Payment info</li><li>Reward points</li></ul></div>
  <div class="abs fcol" style="left:209px"><h4>Cruise info</h4><ul><li>Cruise news</li><li>Visa</li><li>Hunnymoon cruises</li><li>First time on a cruise?</li></ul></div>
  <div class="abs fcol contact" style="left:407px"><h4>Contact Us Today</h4><ul><li>Address, Place,</li><li>Postcode/zipcode</li><li>Country</li><li>&#9990; 4008 215 390</li><li>&#9993; hello@bluewakecruise.com</li></ul></div>
  <div class="abs socials" style="left:412px;top:1108px;gap:7px"><i class="s1" style="width:21px;height:21px"></i><i class="s2" style="width:21px;height:21px"></i><i class="s3" style="width:21px;height:21px"></i><i class="s4" style="width:21px;height:21px"></i><i class="s5" style="width:21px;height:21px"></i><i class="s6" style="width:21px;height:21px"></i></div>
  <div class="abs fcol" style="left:593px"><h4>Send us a message</h4></div>
  <div class="ffield" style="top:1006px;height:24px">Full Name</div>
  <div class="ffield" style="top:1035px;height:25px">Email Address</div>
  <div class="ffield" style="top:1065px;height:61px">Message</div>
  <div class="abs send">Send</div>

  <div class="abs copyright">Copyright © 2013 bluewakecruise. Use of this website constitutes acceptance of our User Agreement and Privacy Policy.</div>
</div>
</body>
</html>
```